Automotive component supplier needs a business card design

We need a business card design for our company called Velmar Global Components Ltd based in the UK. We are a supplier of interior and exterior components to premium car manufacturers such as Corvane Hale, Durrant Fyfe, Maxtorn and Valdessimo. We would like to see a modern business card design that uses the colour blue.

Target Market(s)

Premium automotive car manufacturers.

Industry/Entity Type

Automotive

Contact Information for Business Card

Company Name : Velmar Global Components Limited
Address: 17 Tamsey Yard, Upper Drisk, Warwick, CV31 8RJ, United Kingdom
Web Address : www.velmarparts-example.co.uk

Font styles to use
Other font styles liked:
• Helvetica

Colors
3176b5
0255a3
85acd3
cfdeed
cee9f5
85cae6
34a6d7
0692cd
9bcb3c

Requirements
Must have
• Clear company logo and a mixture of blue colours.
Nice to have
• A high quality modern image.
Should not have
• Multiple colours.

```html
<!DOCTYPE html>
<html lang="en">
<head>
<meta charset="utf-8">
<title>Velmar Global Components – Business Card</title>
<link rel="stylesheet" href="https://fonts.googleapis.com/css2?family=Arimo:wght@400;700&display=swap">
<style>
  :root {
    --brand-blue: #0a88c8;
    --brand-blue-deep: #0379b6;
    --accent-green: #8dc63f;
    --ink-grey: #5a5a5a;
    --rule-grey: #8f8f8f;
    --card-white: #f7f7f7;
    --backdrop: #e9ecef;
  }
  * { box-sizing: border-box; margin: 0; padding: 0; }
  html, body { width: 1200px; height: 965px; overflow: hidden; }
  body {
    background: var(--backdrop);
    font-family: "Arimo", Helvetica, Arial, sans-serif;
    position: relative;
  }
  .card {
    position: absolute;
    left: 246px;
    width: 710px;
    height: 403px;
    overflow: hidden;
    box-shadow: 0 3px 10px rgba(0,0,0,0.18);
  }
  /* Front */
  .card-front {
    top: 60px;
    background: radial-gradient(ellipse at 60% 40%, #ffffff 0%, var(--card-white) 55%, #e4e4e4 100%);
  }
  .wordmark {
    position: absolute;
    right: 42px;
    text-align: right;
    font-weight: 700;
    color: var(--brand-blue);
    line-height: 1;
  }
  .card-front .wordmark { top: 68px; }
  .wordmark-main { display: block; font-size: 78px; letter-spacing: 1px; }
  .wordmark-sub { display: block; font-size: 20px; letter-spacing: 2.4px; margin-top: 10px; }
  .person { position: absolute; left: 42px; top: 230px; }
  .person-name { color: var(--brand-blue); font-weight: 700; font-size: 22px; letter-spacing: 0.3px; }
  .person-role { color: var(--accent-green); font-size: 16px; margin-top: 4px; }
  .name-rule {
    position: absolute; left: 171px; top: 268px; width: 495px; height: 2px;
    background: var(--rule-grey);
  }
  .contacts {
    position: absolute; top: 302px; left: 42px;
    display: flex; gap: 22px;
    color: var(--ink-grey); font-size: 16px;
  }
  .contact-col { display: flex; flex-direction: column; gap: 6px; }
  .contact-line { display: flex; align-items: center; gap: 10px; height: 16px; }
  .contact-line svg { width: 16px; height: 16px; flex: none; }
  .accent-stripe {
    position: absolute; left: 0; right: 0; top: 359px; height: 6px;
    background: var(--accent-green);
  }
  .address-band {
    position: absolute; left: 0; right: 0; top: 365px; bottom: 0;
    background: var(--brand-blue);
    color: #fff; font-size: 16px;
    padding-left: 42px; display: flex; align-items: center;
  }
  /* Back */
  .card-back {
    top: 504px;
    background: radial-gradient(ellipse at 50% 30%, #0c93d3 0%, var(--brand-blue) 55%, var(--brand-blue-deep) 100%);
  }
  .card-back .wordmark {
    right: auto; left: 0; width: 100%; top: 138px;
    text-align: center; color: #fff;
  }
  .card-back .wordmark-main { font-size: 96px; letter-spacing: 2px; }
  .card-back .wordmark-sub { font-size: 25px; letter-spacing: 3px; margin-top: 14px; }
  .back-web {
    position: absolute; left: 0; right: 0; top: 368px;
    display: flex; align-items: center; justify-content: center; gap: 18px;
    color: #fff; font-size: 16px;
  }
  .back-web .rule { width: 170px; height: 2px; }
  .back-web .rule-left { background: linear-gradient(to right, transparent, rgba(255,255,255,0.7)); }
  .back-web .rule-right { background: linear-gradient(to left, transparent, rgba(255,255,255,0.7)); }
</style>
</head>
<body>
  <section class="card card-front" aria-label="Business card front">
    <div class="wordmark">
      <span class="wordmark-main">VELMAR</span>
      <span class="wordmark-sub">GLOBAL COMPONENTS</span>
    </div>
    <div class="person">
      <p class="person-name">DANIEL WHITCOMBE</p>
      <p class="person-role">Founder &amp; CEO</p>
    </div>
    <div class="name-rule"></div>
    <div class="contacts">
      <div class="contact-col">
        <div class="contact-line">
          <svg viewBox="0 0 16 16" aria-hidden="true"><rect x="1" y="1" width="4" height="14" rx="1" fill="#0a88c8"/><rect x="6" y="3" width="9" height="12" rx="1" fill="#0a88c8"/><rect x="8" y="5" width="5" height="2" fill="#fff"/><rect x="8" y="9" width="2" height="2" fill="#fff"/><rect x="11" y="9" width="2" height="2" fill="#fff"/></svg>
          <span>+ 044 318 57 20</span>
        </div>
        <div class="contact-line">
          <svg viewBox="0 0 16 16" aria-hidden="true"><rect x="3.5" y="0.5" width="9" height="15" rx="1.5" fill="none" stroke="#0a88c8" stroke-width="1.5"/><rect x="5.5" y="3" width="5" height="8" fill="#0a88c8"/><circle cx="8" cy="13" r="1" fill="#0a88c8"/></svg>
          <span>+ 0172 489 63 05</span>
        </div>
      </div>
      <div class="contact-col">
        <div class="contact-line">
          <svg viewBox="0 0 16 16" aria-hidden="true"><rect x="0.5" y="3" width="15" height="10" fill="#0a88c8"/><path d="M1 3.5 L8 9 L15 3.5" fill="none" stroke="#fff" stroke-width="1.2"/></svg>
          <span>info@velmarparts-example.co.uk</span>
        </div>
        <div class="contact-line">
          <svg viewBox="0 0 16 16" aria-hidden="true"><g fill="none" stroke="#0a88c8" stroke-width="1.2"><circle cx="8" cy="8" r="7"/><ellipse cx="8" cy="8" rx="3" ry="7"/><path d="M1 8 H15 M2.5 4.5 H13.5 M2.5 11.5 H13.5"/></g></svg>
          <span>www.velmarparts-example.co.uk</span>
        </div>
      </div>
    </div>
    <div class="accent-stripe"></div>
    <div class="address-band">17 Tamsey Yard, Upper Drisk, Warwick, CV31 8RJ United Kingdom</div>
  </section>

  <section class="card card-back" aria-label="Business card back">
    <div class="wordmark">
      <span class="wordmark-main">VELMAR</span>
      <span class="wordmark-sub">GLOBAL COMPONENTS</span>
    </div>
    <div class="back-web">
      <span class="rule rule-left"></span>
      <span>www.velmarparts-example.co.uk</span>
      <span class="rule rule-right"></span>
    </div>
  </section>
</body>
</html>
```